Halvorne Partners Banner Add

We are an international headhunting firm looking to target IT guys in Europe and USA to come and work in Singapore or Sydney (Australia). These guys will generally work in Trading firms / Banks / Top Tech Firms. Text - "Are you working in the Fin/ Tech space for a bank or High Frequency Trading firm as a technologist?We have your job in Singapore/ Sydney.Better / Great LifestyleWorking visa'sThe highest calibre clients.Bored with Brexit?Apply now.We need 5 pictures to rotate on a banner add to attract attention / represent this call to action.Some ideas… Guy on a laptop on a beach Sydney Skyline Singapore Skyline Bondi Beach Paradise beach picturesPeople playing on Beach London in the rain vs Sydney (sunny)Style needs to be classy, premium, well finished, boutique and in keeping with our website www.halvorne-partners.com. - hence any text you think could be worthwhile taking from there is fine.File formats: JPG, PNG, GIF Maximum file size: 3MB Media Sizes: Minimum: 600 × 315 pixels Recommended: 1200 × 628 pixels Image ratio: 1.91:1 To maximize advert delivery, Images need to be public property, no copyright. 5 rotating pictures incorporating the text, pictures and sell to create one banner add.

Target Market(s)

Banking/ Finance

Number of Pages Required

1 page

Requirements
Must have
• 5 different banners on rotate
Nice to have
• Classy, text suggested or snippets of as required, maybe black and white to match our logo's but injections of colour but full colour is also fine I could be converted.
Should not have
• not too flashy, should be elegant, classy pictures, clean like our website.
• www.halvorne-partners.com

```html
<!DOCTYPE html>
<html lang="en">
<head>
<meta charset="utf-8">
<title>Halvorne Partners – Rotating Banner Set</title>
<link href="https://fonts.googleapis.com/css2?family=Roboto+Condensed:wght@400;700&display=swap" rel="stylesheet">
<style>
  :root{
    --page:#ffffff;
    --ink-light:#ffffff;
    --panel-dark:rgba(20,20,20,.72);
    --panel-mid:rgba(60,60,60,.35);
    --panel-light:rgba(255,255,255,.18);
    --brand-box:rgba(255,255,255,.82);
    --brand-ink:#2a2a2a;
    --btn-bg:#0c0c0c;
    --btn-edge:#e9e9e9;
    --accent-blue:rgba(70,120,190,.55);
    --accent-green:rgba(110,200,150,.5);
    --accent-purple:rgba(120,40,110,.55);
    --accent-gold:rgba(190,160,30,.55);
    --accent-red:rgba(200,90,90,.5);
  }
  *{box-sizing:border-box;margin:0;padding:0}
  html,body{width:1200px;height:3462px;overflow:hidden;background:var(--page)}
  body{font-family:"Roboto Condensed",Arial,sans-serif}
  .banner-stack{display:grid;grid-template-rows:repeat(5,628px);row-gap:80.5px;width:1200px}
  .banner{position:relative;width:1200px;height:628px;overflow:hidden}
  .photo{position:absolute;inset:0}
  .photo--harbour-night{background:linear-gradient(180deg,#4a4d52 0%,#2a2c30 45%,#3b4a60 70%,#1b1c1f 100%)}
  .photo--beach-laptop{background:linear-gradient(180deg,#c9c9c9 0%,#a8a8a8 40%,#8c8c8c 55%,#d6d6d6 75%,#bdbdbd 100%)}
  .photo--city-bay{background:linear-gradient(180deg,#d4d4d4 0%,#a9a9a9 45%,#6d6d6d 70%,#3e3e3e 100%)}
  .photo--opera-dusk{background:linear-gradient(180deg,#6a6a6a 0%,#8a8a8a 40%,#3a3a3a 65%,#202020 100%)}
  .photo--ocean-pool{background:linear-gradient(180deg,#bfc3c3 0%,#8c9595 35%,#5f7473 55%,#a8c3bd 80%,#7a8a86 100%)}
  .shapes{position:absolute;inset:0;width:1200px;height:628px}
  .brand{position:absolute;width:402px;height:136px;background:var(--brand-box);display:flex;align-items:center;justify-content:center;gap:16px}
  .brand__mark{width:14px;height:14px;background:var(--brand-ink)}
  .brand__name{font-size:27px;font-weight:400;letter-spacing:.2em;text-transform:uppercase;color:var(--brand-ink)}
  .copy{position:absolute;width:340px;text-align:center;color:var(--ink-light)}
  .copy__text{font-size:24px;line-height:33px;font-weight:400;white-space:nowrap}
  .cta{display:inline-block;margin-top:var(--cta-gap,46px);width:212px;height:52px;line-height:46px;border-radius:26px;background:linear-gradient(180deg,#3a3a3a 0%,var(--btn-bg) 55%);border:3px solid var(--btn-edge);color:var(--ink-light);font-size:19px;font-weight:700;letter-spacing:.04em;text-transform:uppercase;box-shadow:0 3px 6px rgba(0,0,0,.5)}
</style>
</head>
<body>
<main class="banner-stack">

  <section class="banner">
    <div class="photo photo--harbour-night" role="img" aria-label="Black and white night view of Sydney harbour bridge, opera house and city skyline"></div>
    <svg class="shapes" viewBox="0 0 1200 628" aria-hidden="true">
      <polygon points="300,0 750,0 520,314" fill="var(--panel-light)"/>
      <polygon points="340,628 700,628 520,314" fill="var(--accent-blue)"/>
      <polygon points="380,0 660,0 520,314" fill="var(--accent-blue)" opacity=".4"/>
      <polygon points="1000,0 1200,0 1200,628 1000,628 820,314" fill="var(--panel-dark)"/>
      <polygon points="600,0 1000,0 820,314" fill="var(--panel-mid)"/>
    </svg>
    <div class="brand" style="left:30px;top:247px"><span class="brand__mark"></span><span class="brand__name">Halvorne Partners</span></div>
    <div class="copy" style="left:852px;top:187px;--cta-gap:46px">
      <p class="copy__text">Are you working in the FinTech<br>space for a bank or High<br>Frequency Trading firm as<br>a technologist? We have your<br>job in Singapore and Sydney</p>
      <span class="cta">Apply Now</span>
    </div>
  </section>

  <section class="banner">
    <div class="photo photo--beach-laptop" role="img" aria-label="Black and white photo of a man relaxing in a deck chair on a beach with a laptop"></div>
    <svg class="shapes" viewBox="0 0 1200 628" aria-hidden="true">
      <polygon points="450,0 842,0 646,314" fill="var(--accent-green)"/>
      <polygon points="404,628 877,628 646,314" fill="var(--accent-green)"/>
      <polygon points="258,0 520,0 397,314 520,628 258,628" fill="var(--panel-mid)"/>
      <polygon points="0,0 258,0 397,314 258,628 0,628" fill="var(--panel-dark)"/>
    </svg>
    <div class="brand" style="left:773px;top:242px"><span class="brand__mark"></span><span class="brand__name">Halvorne Partners</span></div>
    <div class="copy" style="left:-6px;top:232px;--cta-gap:46px">
      <p class="copy__text">Better and Great<br>Lifestyle</p>
      <span class="cta">Apply Now</span>
    </div>
  </section>

  <section class="banner">
    <div class="photo photo--city-bay" role="img" aria-label="Black and white aerial view of the Singapore bay and skyline"></div>
    <svg class="shapes" viewBox="0 0 1200 628" aria-hidden="true">
      <polygon points="360,0 740,0 545,314" fill="var(--accent-purple)"/>
      <polygon points="320,628 740,628 545,314" fill="var(--accent-purple)"/>
      <polygon points="640,0 923,0 796,314 923,628 640,628 780,314" fill="var(--panel-light)"/>
      <polygon points="923,0 1200,0 1200,628 923,628 796,314" fill="var(--panel-dark)"/>
    </svg>
    <div class="brand" style="left:30px;top:242px"><span class="brand__mark"></span><span class="brand__name">Halvorne Partners</span></div>
    <div class="copy" style="left:858px;top:215px;--cta-gap:46px">
      <p class="copy__text">Apply for a job<br>in Singapore<br>with a working visa</p>
      <span class="cta">Apply Now</span>
    </div>
  </section>

  <section class="banner">
    <div class="photo photo--opera-dusk" role="img" aria-label="Black and white view of the Sydney opera house and harbour at dusk"></div>
    <svg class="shapes" viewBox="0 0 1200 628" aria-hidden="true">
      <polygon points="460,0 860,0 660,314" fill="var(--accent-gold)"/>
      <polygon points="415,628 880,628 660,314" fill="var(--accent-gold)"/>
      <polygon points="270,0 560,0 415,314 560,628 270,628" fill="var(--panel-mid)"/>
      <polygon points="0,0 270,0 415,314 270,628 0,628" fill="var(--panel-dark)"/>
    </svg>
    <div class="brand" style="left:773px;top:254px"><span class="brand__mark"></span><span class="brand__name">Halvorne Partners</span></div>
    <div class="copy" style="left:-5px;top:215px;--cta-gap:46px">
      <p class="copy__text">Bored with Brexit?<br>Come and work in<br>Australia now!</p>
      <span class="cta">Apply Now</span>
    </div>
  </section>

  <section class="banner">
    <div class="photo photo--ocean-pool" role="img" aria-label="Aerial photo of an ocean rock pool with swimmers beside the sea"></div>
    <svg class="shapes" viewBox="0 0 1200 628" aria-hidden="true">
      <polygon points="360,0 740,0 555,314" fill="var(--accent-red)"/>
      <polygon points="330,628 760,628 555,314" fill="var(--accent-red)"/>
      <polygon points="660,0 923,0 808,314 923,628 660,628 790,314" fill="var(--panel-light)"/>
      <polygon points="923,0 1200,0 1200,628 923,628 808,314" fill="var(--panel-dark)"/>
    </svg>
    <div class="brand" style="left:30px;top:242px"><span class="brand__mark"></span><span class="brand__name">Halvorne Partners</span></div>
    <div class="copy" style="left:850px;top:187px;--cta-gap:32px">
      <p class="copy__text" style="font-size:23px">We know where to find the<br>specialists you need and<br>selectively partner with<br>organizations to locate, entice<br>and secure the very best talent.</p>
      <span class="cta">Apply Now</span>
    </div>
  </section>

</main>
</body>
</html>
```